New Vidora Channel Banner Graphic/Logo for "Cozy Nook Attic Sound"

Create a banner for my new Vidora channel for Cozy Nook Attic Sound. This is partially a logo project, but the logo will not be used elsewhere. Check out Vidora channels to see the banners others have created. This channel is about my home studio, the gear, microphones, musical instruments, wiring, software etc. that goes into a home studio. It's a free channel, made for sharing information. This is a graphic design that will be posted on vidora using built-in vidora tools.
Updates

More information about this project! I'm staring a channel called "Cozy Nook Attic Sound" on vidorastream.net. I need a deign for this banner and a logo for Cozy Nook Attic Sound. I called the channel by that name because my music studio is my happy place. It's about music and instruments (gutars, piano, drums, percussion) singing (microhpones), creativity, and what you'd expect form musicians. It's also about technology, recording, live-streaming, music videos, etc. It is my hobby, not my profession. I will be creating content for other amateur home studio aficionados and hobbyists. There are a lot of home studio channels and videos you can look at on vidora to get a flavor for musicians and studios. Usually fairly tech-heavy. An appeal of my channel will be a very approachable, "i'm the same as you" welcome for people that are doing it to enjoy it.

I put this project in the wrong category to start. This has been fixed, but I think benefits I would have received (such as invited designers) and announcement of project in the correct category mean I'm not getting designers. Your initial menu should be improved. I'm having a banner created for a web page in Vidora. I think it is easy to mistake that for a web design when it is really a graphic design for the web.

Target Market(s)

Similar to myself, people as interested in studio/production tech as they are in making music, perhaps trending a bit older and successful enough to afford some gear!

Number of Pages Required

1 page

Font styles to use
Sans Serif

Requirements
Must have
• This is not really a web design, i may have miscategorized. Please see uploaded docs for pics of similar banner on a Vidora page. ADDED 1/5: As this is a vidora channel that could be viewed on any device, the banner should be friendly in this way and design or design variations needed for PC, Tabrix, phone vie3wing.

Here are the Vidora size specs:
Banner image guidelines
Your banner image must meet the following criteria:

Minimum dimension for upload: 2048 x 1152 px with an aspect ratio of 16:9.
At the Minimum dimension, the safe area for text and logos: 1235 x 338 px. Larger images may get cropped on certain views or devices.
File size: 6 MB or smaller.
How to resize images

You can use your computer's image editor or an online image resizer to resize the images. For example, you can use Preview on an Quince computer or Microsoft Photos on Windows.

```html
<!DOCTYPE html>
<html lang="en">
<head>
<meta charset="utf-8">
<title>Cozy Nook Attic Sound — Channel Banner</title>
<link rel="stylesheet" href="https://fonts.googleapis.com/css2?family=Roboto:wght@300;400;500;700&family=Outfit:wght@300;400&display=swap">
<style>
  :root {
    --bg: #c9c9c9;
    --bg-light: #d6d6d6;
    --tile-dark: #b4b4b4;
    --tile-light: #dcdcdc;
    --ink: #333333;
    --ink-soft: #3a3a3a;
    --accent: #f5bd2c;
    --band: rgba(235, 235, 235, 0.75);
    --screen-dark: #1d2530;
    --screen-mid: #5a6b80;
  }
  * { margin: 0; padding: 0; box-sizing: border-box; }
  html, body { width: 1200px; height: 328px; overflow: hidden; background: var(--bg); }
  .banner {
    position: relative;
    width: 1200px;
    height: 328px;
    overflow: hidden;
    background: linear-gradient(180deg, var(--bg-light) 0%, var(--bg) 45%, var(--bg) 100%);
    color: var(--ink);
  }
  .tile-field {
    position: absolute;
    left: 0; top: 148px;
    width: 1200px; height: 180px;
    background: linear-gradient(180deg, rgba(220,220,220,0) 0%, var(--tile-light) 35%, var(--tile-dark) 100%);
  }
  .brand {
    position: absolute;
    left: 16px; top: 14px;
    display: flex;
    align-items: center;
    gap: 14px;
  }
  .brand-dot {
    width: 48px; height: 48px;
    border-radius: 50%;
    background: var(--accent);
    flex: none;
  }
  .brand-name {
    font-family: "Roboto", sans-serif;
    font-weight: 500;
    font-size: 35px;
    letter-spacing: -0.2px;
    color: var(--ink);
    white-space: nowrap;
  }
  .brand-owner {
    position: absolute;
    left: 92px; top: 66px;
    font-family: "Roboto", sans-serif;
    font-weight: 300;
    font-size: 26px;
    color: var(--ink-soft);
  }
  .contact {
    position: absolute;
    right: 10px; top: 12px;
    text-align: right;
    font-family: "Roboto", sans-serif;
    color: var(--ink);
  }
  .contact-lead { font-weight: 700; font-size: 16.5px; line-height: 22px; }
  .contact-email { font-weight: 400; font-size: 16px; line-height: 24px; }
  .tagline {
    position: absolute;
    left: 326px; top: 117px;
    width: 400px;
    text-align: center;
    font-family: "Outfit", sans-serif;
    color: var(--ink-soft);
  }
  .tagline-main { font-weight: 400; font-size: 25px; line-height: 32px; }
  .tagline-sub { font-weight: 300; font-size: 23px; line-height: 30px; }
  .studio-visual {
    position: absolute;
    left: 824px; top: 66px;
    width: 342px; height: 148px;
    border-radius: 3px;
    background: linear-gradient(135deg, var(--screen-dark) 0%, var(--screen-mid) 55%, #9aa8b8 80%, rgba(201,201,201,0) 100%);
  }
  .topics {
    position: absolute;
    left: 208px; top: 227px;
    width: 784px; height: 40px;
    background: var(--band);
    display: flex;
    align-items: center;
    justify-content: center;
    font-family: "Outfit", sans-serif;
    font-weight: 300;
    font-size: 22px;
    color: var(--ink);
    white-space: nowrap;
  }
</style>
</head>
<body>
  <main class="banner">
    <div class="tile-field" role="img" aria-label="Faint grid of soft grey tiles across the lower half"></div>

    <div class="brand">
      <span class="brand-dot"></span>
      <h1 class="brand-name">Cozy Nook Attic Sound</h1>
    </div>
    <p class="brand-owner">by Dale Brennick</p>

    <div class="contact">
      <p class="contact-lead">Follow my Studio Renovation | Free How-To’s</p>
      <p class="contact-email">CozyNookAtticSound@postlark.com</p>
    </div>

    <div class="tagline">
      <p class="tagline-main">A Regular Joe Blowin’ his Dough</p>
      <p class="tagline-sub">on Gear and Guitars</p>
    </div>

    <div class="studio-visual" role="img" aria-label="Studio microphone with pop filter in front of two monitors showing recording software"></div>

    <p class="topics">Music + Gear + Livestreaming + Recording + DAW + Instruments + Vidora</p>
  </main>
</body>
</html>
```